Artificial intelligence, machine learning, and automation company needs a sexy business card design

We need a sleek and sexy business card design for an AI consulting company based in Philadelphia PA. We provide custom machine learning and automation solutions for companies of all shapes and sizes. The primary industries that we serve are pharmaceuticals, engineering, healthcare, and computer software. We would like the designs to be a black business card that uses green as a sleek accent color. The final design should communicate intelligence, cutting edge new-tech, and optimization.

Target Market(s)

C-level and VP level executives of multi-million annual companies. Mostly in Pharma, Healthcare, Real Estate, Retail, and Engineering

Industry/Entity Type

Computer Software

Contact Information for Business Card

Name: Jack Moss
Title: CEO
Cell: 215 604 8293
Email: JackM@quillarcworks.example
Website: www.QuillarcWorks.example

Font styles to use
Sans Serif

Colors

Designer to choose colors to be used in the design.

Requirements
Must have
• 1) Attached Quillarc Logo (either with colors or not/embossed)
• 2) "Artificial Intelligence" "Automation" and "Machine Learning"
• 3) "Quillarc Laboratories" or "Quillarc Works" or "Quillarc"
• 4) Sexy AF.
Nice to have
• Black card / dark card color, "Quillarc Green" accent colors (in attached .ai file), Embossment of logo/name/etc, thick card stock, colored borders (on card sides, not front/back faces)
Should not have
• Should not be bland, or unsexy.

```html
<!DOCTYPE html>
<html lang="en">
<head>
<meta charset="utf-8">
<title>Quillarc Works Business Card</title>
<link href="https://fonts.googleapis.com/css2?family=Roboto:wght@300;400&display=swap" rel="stylesheet">
<style>
  :root {
    --backdrop: #ecebe8;
    --quillarc-green: #4faaa1;
    --card-black: #1f1e20;
    --ink-dark: #2c3837;
    --ink-line: #3a4a48;
    --mark-grey: #6d6d70;
  }
  * { box-sizing: border-box; margin: 0; padding: 0; }
  html, body {
    width: 1200px;
    height: 800px;
    overflow: hidden;
    background: var(--backdrop);
    font-family: "Roboto", sans-serif;
  }
  .canvas {
    width: 1200px;
    height: 800px;
    display: flex;
    align-items: center;
    justify-content: center;
    gap: 48px;
  }
  .card {
    position: relative;
    width: 540px;
    height: 309px;
    box-shadow: 0 10px 24px rgba(0, 0, 0, 0.28);
    overflow: hidden;
  }

  /* Contact side */
  .card--contact {
    background: var(--quillarc-green);
    color: var(--ink-dark);
  }
  .rule {
    position: absolute;
    left: 34px;
    right: 34px;
    height: 1px;
    background: var(--ink-line);
  }
  .rule--top { top: 54px; }
  .rule--bottom { bottom: 48px; }
  .identity {
    position: absolute;
    top: 128px;
    right: 300px;
    text-align: right;
    font-weight: 400;
    font-size: 19px;
    line-height: 24px;
  }
  .contact-list {
    position: absolute;
    top: 110px;
    left: 262px;
    list-style: none;
    font-size: 13px;
    font-weight: 300;
    line-height: 23px;
  }
  .contact-list li {
    display: flex;
    align-items: center;
    gap: 9px;
    white-space: nowrap;
  }
  .contact-list svg {
    width: 11px;
    height: 11px;
    flex: none;
  }
  .address {
    position: absolute;
    left: 60px;
    bottom: 58px;
    font-size: 12px;
    font-weight: 300;
  }

  /* Brand side */
  .card--brand {
    background: var(--card-black);
  }
  .corner-accent {
    position: absolute;
    top: 0;
    right: 0;
    width: 62px;
    height: 62px;
  }
  .brand-lockup {
    position: absolute;
    inset: 0;
    display: flex;
    flex-direction: column;
    align-items: center;
    justify-content: center;
  }
  .brand-square {
    width: 72px;
    height: 72px;
    border: 3px solid var(--mark-grey);
    margin-bottom: 10px;
  }
  .brand-name {
    color: var(--mark-grey);
    font-weight: 400;
    font-size: 20px;
    letter-spacing: 5px;
    line-height: 22px;
    text-align: center;
    padding-left: 5px;
  }
  .brand-sub {
    color: var(--mark-grey);
    font-weight: 400;
    font-size: 8px;
    letter-spacing: 2.6px;
    line-height: 12px;
    text-align: center;
    padding-left: 2.6px;
  }
  .brand-services {
    position: absolute;
    left: 0;
    right: 0;
    bottom: 30px;
    color: var(--quillarc-green);
    font-weight: 300;
    font-size: 9px;
    letter-spacing: 2.4px;
    text-align: center;
    text-transform: uppercase;
  }
</style>
</head>
<body>
<main class="canvas">

  <section class="card card--contact" aria-label="Contact side">
    <div class="rule rule--top"></div>
    <div class="identity">
      <p class="identity-name">Jack Moss</p>
      <p class="identity-title">CEO</p>
    </div>
    <ul class="contact-list">
      <li>
        <svg viewBox="0 0 12 12" aria-hidden="true"><circle cx="6" cy="6" r="5.3" fill="none" stroke="currentColor" stroke-width="1"/><path d="M4 3.4c.4-.3.7-.2.9.2l.4.8c.1.3 0 .5-.2.7l-.3.2c.3.7.8 1.2 1.5 1.5l.2-.3c.2-.2.4-.3.7-.2l.8.4c.4.2.5.5.2.9-.4.6-1 .8-1.7.5C5.5 7.6 4.4 6.5 3.8 5.1c-.3-.7-.3-1.3.2-1.7z" fill="currentColor"/></svg>
        215 604 8293
      </li>
      <li>
        <svg viewBox="0 0 12 12" aria-hidden="true"><circle cx="6" cy="6" r="6" fill="currentColor"/><rect x="3" y="4" width="6" height="4" fill="none" stroke="var(--quillarc-green)" stroke-width="0.9"/><path d="M3 4l3 2.2L9 4" fill="none" stroke="var(--quillarc-green)" stroke-width="0.9"/></svg>
        JackM@quillarcworks.example
      </li>
      <li>
        <svg viewBox="0 0 12 12" aria-hidden="true"><circle cx="6" cy="6" r="6" fill="currentColor" opacity="0.75"/></svg>
        www.QuillarcWorks.example
      </li>
    </ul>
    <p class="address">2750 Larchmont St, Philadelphia, PA 19130</p>
    <div class="rule rule--bottom"></div>
  </section>

  <section class="card card--brand" aria-label="Brand side">
    <svg class="corner-accent" viewBox="0 0 62 62" aria-hidden="true">
      <polygon points="0,0 62,0 62,62" fill="var(--quillarc-green)"/>
    </svg>
    <div class="brand-lockup">
      <div class="brand-square" aria-hidden="true"></div>
      <p class="brand-name">QUILLARC</p>
      <p class="brand-sub">LABORATORIES</p>
    </div>
    <p class="brand-services">Artificial Intelligence · Machine Learning · Automation</p>
  </section>

</main>
</body>
</html>
```